Hamper box design

We are a chocolate business and need a sophisticated, premium hamper box design. Our hamper box is black and we tie a ribbon on the outside (please see attached photo).

Requirements:
- Incorporate our logo or picture of bean on the top surface of the hamper box
- Need a design for the inside of the top lid (see attachment "Inside Design" for an example)

The dimensions of the actual hamper boxes (need the correct files for these sizes):
1. 240mm wide x 210mm long x 60mm deep.
2. 340mm wide x 260mm long x 90mm deep.
3. 420mm wide x 330mm long x 110mm deep.

Suggestions (not essential):
- Where Chocolate Meets Craftmanship (our slogan)
- The smoothest French chocolate experience
- A thin gold border styling on the top and/or inside surface (to give sophisticated feel) See "Tobias Wrenfield border" file
- Follow us:
(instagram symbol) @brindlewoodtreats
(facebook symbol) facebook.com/brindlewoodtreats
(world symbol) www.brindlewoodtreats.com.au

Our website is: www.brindlewoodtreats.com.au
Potential inspiration from our instagram.com/brindlewoodtreats

```html
<!DOCTYPE html>
<html lang="en">
<head>
<meta charset="utf-8">
<title>Brindlewood Treats – Inside Lid Design</title>
<link rel="stylesheet" href="https://fonts.googleapis.com/css2?family=Satisfy&display=swap">
<style>
  :root {
    --page-bg: #ffffff;
    --slate: #23282b;
    --slate-deep: #1a1d1f;
    --cocoa-dark: #3a2118;
    --cocoa-mid: #6b3f2c;
    --cocoa-light: #9a6447;
    --copper: #dc8c73;
  }

  html, body {
    margin: 0;
    padding: 0;
    width: 1200px;
    height: 800px;
    overflow: hidden;
    background: var(--page-bg);
  }

  .canvas {
    position: relative;
    width: 1200px;
    height: 800px;
    display: flex;
    align-items: center;
    justify-content: center;
  }

  .lid-inside {
    position: relative;
    width: 960px;
    height: 733px;
    overflow: hidden;
  }

  .chocolate-backdrop {
    position: absolute;
    inset: 0;
    background:
      radial-gradient(ellipse 52% 44% at 52% 50%, var(--slate) 0%, var(--slate) 55%, rgba(35, 40, 43, 0) 100%),
      linear-gradient(135deg, var(--cocoa-light) 0%, var(--cocoa-dark) 30%, var(--cocoa-mid) 50%, var(--cocoa-dark) 70%, var(--cocoa-light) 100%);
    background-color: var(--slate-deep);
  }

  .slogan {
    position: absolute;
    inset: 0;
    margin: 0;
    font-family: "Satisfy", cursive;
    font-weight: 400;
    color: var(--copper);
    text-align: center;
  }

  .slogan-line {
    position: absolute;
    left: 0;
    right: 0;
    display: block;
    line-height: 1;
    transform: translateX(20px);
  }

  .slogan-where {
    top: 230px;
    font-size: 58px;
  }

  .slogan-meets {
    top: 292px;
    font-size: 70px;
  }

  .slogan-craft {
    top: 380px;
    font-size: 104px;
    transform: translateX(26px);
  }
</style>
</head>
<body>
  <main class="canvas">
    <section class="lid-inside">
      <div class="chocolate-backdrop" role="img" aria-label="Broken pieces of milk and dark chocolate scattered around the edges of a dark slate surface"></div>
      <h1 class="slogan">
        <span class="slogan-line slogan-where">Where</span>
        <span class="slogan-line slogan-meets">Chocolate Meets</span>
        <span class="slogan-line slogan-craft">Craftmanship</span>
      </h1>
    </section>
  </main>
</body>
</html>
```